OPF - Brochure 52 week Curriculum

Oak Path Fellows, Inc. wants to create a distribution Brochure. In the Bible (Matthew 28:18-20)- JESUS said to "TEACH" others what HE has commanded. we want to "PUT IN PRINT"

these 52 lines summarize HIS teachings
we want to use as our Curriculum teaching men ...

incorporate our statements and two main passages of scripture
(see attach pictures of headquarter lobby) to brand uniformity and consistency... we have summarized into 52 groups, but its NOT required to have numbers...
Purpose = obey GOD
Mission = love others
Vision = Development God fearing men globally.

The designer can have freedom in layout and sizing.
we were thinking bi fold , but again... designer has freedom
Please incorporate our colors (white, black, gray) using color wheel provided and our LOGO with website.

```html
<!DOCTYPE html>
<html lang="en">
<head>
<meta charset="utf-8">
<title>Oak Path Fellows – Curriculum Brochure Spread</title>
<link rel="stylesheet" href="https://fonts.googleapis.com/css2?family=Poppins:ital,wght@0,400;0,500;0,700;0,800;1,400&display=swap">
<style>
  :root {
    --canvas: #e6e9ea;
    --ink-black: #1c1c1c;
    --page-dark: #262626;
    --page-dark-2: #333333;
    --photo-dark: #4a4a4a;
    --photo-mid: #8d8d8d;
    --photo-light: #b9b9b9;
    --panel: rgba(226, 226, 224, 0.9);
    --white: #ffffff;
    --soft-white: #e4e4e4;
    --gray-text: #b0b0b0;
    --dark-text: #2a2a2a;
  }
  * { box-sizing: border-box; margin: 0; padding: 0; }
  html, body { width: 1200px; height: 700px; overflow: hidden; }
  body {
    background: var(--canvas);
    font-family: "Poppins", sans-serif;
    display: flex; align-items: center; justify-content: center;
  }
  .spread {
    width: 1120px; height: 410px;
    display: flex;
    box-shadow: 0 14px 30px rgba(0,0,0,0.18);
  }
  .page { position: relative; width: 560px; height: 410px; overflow: hidden; }

  /* Left page */
  .page--prayer { background: linear-gradient(90deg, var(--page-dark) 0%, var(--page-dark-2) 60%, var(--page-dark) 100%); }
  .page--prayer .photo {
    position: absolute; left: 0; top: 0; width: 300px; height: 100%;
    background: radial-gradient(ellipse at 45% 55%, #9a9a9a 0%, #5c5c5c 35%, #2f2f2f 70%, var(--page-dark) 100%);
  }
  .page--prayer .content {
    position: absolute; left: 262px; top: 48px; width: 276px;
  }
  .section-title {
    font-weight: 800; font-size: 22px; letter-spacing: 0.5px; line-height: 1.05;
    text-transform: uppercase;
  }
  .page--prayer .section-title { color: var(--soft-white); margin-bottom: 12px; }
  .points { list-style: none; }
  .points li {
    display: flex; gap: 9px; align-items: flex-start;
    font-size: 9.6px; line-height: 1.35; margin-bottom: 8px;
  }
  .page--prayer .points li { color: var(--gray-text); font-style: italic; }
  .points svg { flex: 0 0 12px; width: 12px; height: 12px; margin-top: 2px; }

  .brand-name {
    position: absolute; left: 24px; bottom: 20px;
    font-weight: 800; font-size: 20px; letter-spacing: 0.5px;
  }
  .page--prayer .brand-name { color: var(--white); }
  .folio {
    position: absolute; bottom: 24px; font-size: 10px; letter-spacing: 0.3px;
  }
  .folio b { font-weight: 700; }
  .folio .sep { margin: 0 12px; }
  .page--prayer .folio { right: 26px; color: var(--gray-text); }

  /* Right page */
  .page--outreach {
    background: linear-gradient(100deg, var(--photo-light) 0%, var(--photo-mid) 45%, var(--photo-dark) 80%, #3a3a3a 100%);
  }
  .page--outreach .photo {
    position: absolute; inset: 0;
    background: radial-gradient(ellipse at 65% 55%, #cfcfcf 0%, #8a8a8a 30%, #4d4d4d 65%, #3b3b3b 100%);
  }
  .page--outreach .panel {
    position: absolute; left: 22px; top: 0; width: 285px; height: 300px;
    background: var(--panel);
    padding: 42px 22px 0 22px;
  }
  .page--outreach .section-title { color: var(--dark-text); margin-bottom: 14px; font-size: 20px; }
  .page--outreach .points li { color: var(--dark-text); }
  .page--outreach .brand-name { color: var(--ink-black); bottom: 22px; left: 34px; }
  .page--outreach .folio { right: 24px; bottom: 140px; color: var(--soft-white); }
</style>
</head>
<body>
  <main class="spread">
    <section class="page page--prayer">
      <div class="photo" role="img" aria-label="Black and white photo of a man praying with clasped hands holding a cross"></div>
      <div class="content">
        <h2 class="section-title">Prayer</h2>
        <ul class="points">
          <li><svg viewBox="0 0 12 12"><path d="M1 2l5 4-5 4z M5 2l5 4-5 4z" fill="#ffffff"/></svg><span>Jesus provided guidance on prayer, teaching that it should be done in private and with sincerity (Matthew 6:5–8).</span></li>
          <li><svg viewBox="0 0 12 12"><path d="M1 2l5 4-5 4z M5 2l5 4-5 4z" fill="#ffffff"/></svg><span>He also linked prayer to having a forgiving heart (Mark 11:25; Matthew 18:18–20). HE encouraged praying with simple faith and persistence (Luke 11:5–13; Matthew 21:21–22).</span></li>
          <li><svg viewBox="0 0 12 12"><path d="M1 2l5 4-5 4z M5 2l5 4-5 4z" fill="#ffffff"/></svg><span>Pray: Engage in prayer consistently, with sincerity and according to Jesus’ example.</span></li>
          <li><svg viewBox="0 0 12 12"><path d="M1 2l5 4-5 4z M5 2l5 4-5 4z" fill="#ffffff"/></svg><span>Prayer for our enemies : Luke 23:24, Matthew 5:44</span></li>
          <li><svg viewBox="0 0 12 12"><path d="M1 2l5 4-5 4z M5 2l5 4-5 4z" fill="#ffffff"/></svg><span>Pray for others : intercession</span></li>
          <li><svg viewBox="0 0 12 12"><path d="M1 2l5 4-5 4z M5 2l5 4-5 4z" fill="#ffffff"/></svg><span>Pray for laborers: Seek God to send workers into the harvest field of souls. Pray for kingdom laborers: Matthew 9:38, Luke 10:2</span></li>
        </ul>
      </div>
      <div class="brand-name">OPF</div>
      <p class="folio"><b>Page 8</b><span class="sep">|</span>oakpathfellows.org</p>
    </section>

    <section class="page page--outreach">
      <div class="photo" role="img" aria-label="Black and white photo of two men seated side by side holding hands in prayer"></div>
      <div class="panel">
        <h2 class="section-title">Regarding Outreach<br>and Discipleship</h2>
        <ul class="points">
          <li><svg viewBox="0 0 12 12"><path d="M1 2l5 4-5 4z M5 2l5 4-5 4z" fill="#1c1c1c"/></svg><span>Go and make disciples of all nations: Evangelize and teach others to follow Jesus’ commands: This is a central command, emphasizing the importance of evangelism and discipleship. Matthew 28:18-20. Teach others to obey all that Jesus commanded. Passing on the teachings of Christ to new believers is a key aspect of discipleship.</span></li>
          <li><svg viewBox="0 0 12 12"><path d="M1 2l5 4-5 4z M5 2l5 4-5 4z" fill="#1c1c1c"/></svg><span>Feed My Sheep: Care for and nourish the spiritual lives of believers.</span></li>
          <li><svg viewBox="0 0 12 12"><path d="M1 2l5 4-5 4z M5 2l5 4-5 4z" fill="#1c1c1c"/></svg><span>Receive God’s power. Be filled with the Holy Spirit to effectively carry out God’s work.</span></li>
        </ul>
      </div>
      <div class="brand-name">OPF</div>
      <p class="folio"><b>Page 9</b><span class="sep">|</span>oakpathfellows.org</p>
    </section>
  </main>
</body>
</html>
```